Environmental Group Website Template

We want a website template for an environmental cause. The website should have a dark content area that is transparent. The website text and icons are white.
The background is a nature scene. The background image repeats.
Industry/Entity Type
Group

```html
<!DOCTYPE html>
<html lang="en">
<head>
<meta charset="utf-8">
<title>Green Cause – Home</title>
<link rel="stylesheet" href="https://fonts.googleapis.com/css2?family=Roboto:wght@400;500;700&family=Arimo:wght@400;700&display=swap">
<style>
  :root{
    --orange:#f4612c;
    --orange-light:#ff7a3d;
    --green-1:#52b03e;
    --green-2:#7dc226;
    --green-3:#a1cb06;
    --underline:#6cc04a;
    --ink:#2b2b2b;
    --body:#555;
    --white:#fff;
    --footer-top:#4a4a4a;
    --footer-bottom:#1c1c1c;
  }
  *{box-sizing:border-box;margin:0;padding:0}
  html,body{width:1200px;height:1126px;overflow:hidden}
  body{position:relative;font-family:"Arimo",Arial,sans-serif;color:var(--body)}
  .backdrop{position:absolute;inset:0;
    background:linear-gradient(180deg,#9cc46a 0%,#dfe7d2 24%,#8eaa4a 30%,#7ea33e 40%,#5d6f86 50%,#7b8da2 62%,#5f7088 74%,#8ca45a 86%,#6d8a3a 100%);}
  .page{position:absolute;left:171px;top:28px;width:858px;height:1098px}
  .masthead{height:126px;position:relative;
    background:linear-gradient(180deg,rgba(240,246,236,.85),rgba(255,255,255,.95))}
  .brand{position:absolute;left:14px;top:22px;display:flex;align-items:center;gap:10px}
  .brand-dot{width:70px;height:70px;border-radius:50%;background:var(--orange)}
  .brand-name{font-family:"Roboto",sans-serif;font-weight:400;font-size:21px;line-height:25px;color:#333;text-align:center;letter-spacing:-.3px}
  .search{position:absolute;left:646px;top:53px;width:182px;height:34px;background:#fff;border:1px solid #ccc;border-radius:2px;display:flex;align-items:center;justify-content:space-between;padding:0 9px 0 8px;font-size:12px;color:#888}
  .nav{height:47px;background:linear-gradient(180deg,var(--orange-light),var(--orange));position:relative}
  .nav a{position:absolute;top:15px;font-family:"Roboto",sans-serif;font-weight:700;font-size:12.5px;color:var(--white);text-decoration:none}
  .nav .active::after{content:"";position:absolute;left:-14px;right:-17px;top:28px;height:3px;background:var(--underline)}
  .hero{height:452px;position:relative;
    background:linear-gradient(180deg,#8f9560 0%,#6e7f52 25%,#55676a 50%,#4a5a6c 75%,#3e4c5c 100%)}
  .caption{position:absolute;left:0;top:318px;width:411px;height:87px;background:rgba(60,40,40,.55);padding:8px 12px}
  .caption h1{font-family:"Roboto",sans-serif;font-weight:700;font-size:25px;color:var(--white);letter-spacing:.3px;margin-bottom:4px;white-space:nowrap}
  .caption p{font-size:11px;line-height:19px;color:var(--white)}
  .dots{position:absolute;left:15px;top:417px;display:flex;gap:11px}
  .dots span{width:13px;height:13px;border-radius:50%;background:var(--white)}
  .dots .on{background:var(--orange);border:2px solid var(--white)}
  .features{display:flex;height:178px}
  .feature{flex:0 0 auto;text-align:center;color:var(--white);padding-top:18px}
  .feature:nth-child(1){width:286px;background:var(--green-1)}
  .feature:nth-child(2){width:287px;background:var(--green-2)}
  .feature:nth-child(3){width:285px;background:var(--green-3)}
  .feature svg{height:44px;width:50px;display:block;margin:0 auto}
  .feature h2{font-family:"Roboto",sans-serif;font-weight:500;font-size:16px;color:var(--ink);margin:9px 0 2px;letter-spacing:.3px}
  .feature p{font-size:11px;line-height:18px;padding:0 38px}
  .feature .more{display:inline-block;margin-top:7px;font-size:11px;font-weight:700;color:var(--orange)}
  .about{height:216px;background:rgba(240,242,245,.9);text-align:center;padding-top:30px}
  .about h2{font-family:"Roboto",sans-serif;font-weight:500;font-size:26px;color:var(--ink);letter-spacing:.5px}
  .about h2 span{color:var(--orange)}
  .about p{font-size:12px;line-height:20.5px;letter-spacing:.3px;padding:0 50px;margin-top:9px;color:var(--body)}
  .btn{display:inline-flex;align-items:center;gap:7px;margin-top:14px;height:32px;padding:0 8px 0 11px;background:#2a2a2a;border-radius:2px;color:var(--white);font-family:"Roboto",sans-serif;font-weight:500;font-size:12px}
  .footer{height:79px;background:linear-gradient(180deg,var(--footer-top),var(--footer-bottom));display:flex;align-items:center;justify-content:space-between;padding:0 17px 0 19px}
  .social{display:flex;gap:10px}
  .social span{width:27px;height:27px;border-radius:3px}
  .copy{font-size:11px;color:var(--white)}
</style>
</head>
<body>
<div class="backdrop" role="img" aria-label="Repeating nature scene of marsh grass, leaves and water"></div>
<div class="page">
  <header class="masthead">
    <div class="brand"><span class="brand-dot"></span><span class="brand-name">YOUR LOGO<br>HERE</span></div>
    <div class="search">Search...
      <svg width="18" height="18" viewBox="0 0 20 20"><circle cx="8" cy="8" r="6" fill="none" stroke="#222" stroke-width="2.6"/><line x1="12.5" y1="12.5" x2="18" y2="18" stroke="#222" stroke-width="3" stroke-linecap="round"/></svg>
    </div>
  </header>
  <nav class="nav">
    <a class="active" href="#" style="left:29px">Home</a>
    <a href="#" style="left:109px">About</a>
    <a href="#" style="left:192px">Explore</a>
    <a href="#" style="left:283px">Challenses</a>
    <a href="#" style="left:396px">Solutions</a>
    <a href="#" style="left:499px">Events</a>
    <a href="#" style="left:586px">News</a>
  </nav>
  <section class="hero" role="img" aria-label="Photo of a family paddling a canoe on a lake">
    <div class="caption">
      <h1>Let us take care of your trees!</h1>
      <p>Lorem ipsum dolor sit amet, consectetur adipiscing elit, sed do eiusmod tempor incididunt ut labore et dolore magna aliqua.</p>
    </div>
    <div class="dots"><span></span><span class="on"></span><span></span><span></span></div>
  </section>
  <section class="features">
    <div class="feature">
      <svg viewBox="0 0 50 44" fill="none" stroke="#fff" stroke-width="2.2"><circle cx="17" cy="8" r="5"/><circle cx="33" cy="8" r="5"/><path d="M8 42V24l6-8h6l5 10 5-10h6l6 8v18M18 42V30M32 42V30"/></svg>
      <h2>Volunteers</h2>
      <p>Lorem ipsum dolor sit amet, consectetur incididunt ut labore et dolore magna aliqua Ut enim</p>
      <span class="more">Read More »</span>
    </div>
    <div class="feature">
      <svg viewBox="0 0 50 44" fill="#fff"><circle cx="30" cy="14" r="11"/><circle cx="30" cy="14" r="5" fill="#7dc226"/><path d="M3 30h10l8 3h10c3 0 3 4 0 4H20h12l12-7c3-1 4 2 2 4l-13 9H14l-6-3H3z"/></svg>
      <h2>Spport Our Work</h2>
      <p>Lorem ipsum dolor sit amet, consectetur incididunt ut labore et dolore magna aliqua Ut enim</p>
      <span class="more">Read More »</span>
    </div>
    <div class="feature">
      <svg viewBox="0 0 50 44" fill="none" stroke="#fff" stroke-width="2.2"><path d="M6 14h8l22-11v34L14 26H6z"/><path d="M40 14a6 6 0 0 1 0 12"/><path d="M14 26l3 14h6l-2-14"/></svg>
      <h2>Make your voice heard</h2>
      <p>Lorem ipsum dolor sit amet, consectetur incididunt ut labore et dolore magna aliqua Ut enim</p>
      <span class="more">Read More »</span>
    </div>
  </section>
  <section class="about">
    <h2>About <span>Logo Here</span></h2>
    <p>Lorem ipsum dolor sit amet, consectetur adipiscing elit, sed do eiusmod tempor incididunt ut labore et dolore magna aliqua. Ut enim ad minim velit esse cillum dolore eu fugiat nulla pariatur. Excepteur sint occaecat cupidatat non proident, sunt in culpa qui officia deserunt mollit anim id est laborum Sed ut perspiciatis unde omnis iste natus error sit voluptatem doloremque.</p>
    <span class="btn">Read More
      <svg width="14" height="14" viewBox="0 0 14 14" fill="none" stroke="#fff" stroke-width="1.3"><circle cx="7" cy="7" r="6"/><path d="M6 4l3 3-3 3"/></svg>
    </span>
  </section>
  <footer class="footer">
    <div class="social">
      <span style="background:#3b5a9a"></span><span style="background:#29a9e1"></span><span style="background:#f28a1e"></span><span style="background:#d6492f"></span><span style="background:#c9202a"></span><span style="background:#0b7bb5"></span>
    </div>
    <div class="copy">Copyright © 2014. All Rights Reserved.</div>
  </footer>
</div>
</body>
</html>
```